Premium Coffee Business Needs a Wordpress Design

We need a Wordpress design for a Premium Coffee E-commerce based in Sao Paulo, Brazil. We want something very similar to tallowfinchroasters.com, but with a few exceptions, better described in the attachment (PLEASE READ our specifications). The product we're selling is premium, so we need to communicate sophistication, and at the same time people should feel they're in contact with an innovative company. Our company is called Coffee Meridian.
Adults aged 25 to 50 who have refined tastes.
Business

```html
<!DOCTYPE html>
<html lang="en">
<head>
<meta charset="utf-8">
<title>Coffee Meridian</title>
<link href="https://fonts.googleapis.com/css2?family=Arimo:wght@400;700&display=swap" rel="stylesheet">
<style>
:root{
  --brown-dark:#4a2a14;
  --brown-deep:#5a2d0c;
  --amber:#8f4a07;
  --amber-shade:#6e3805;
  --copper:#d08a3c;
  --band:#e9e9e9;
  --hex-shadow:#d9d9d9;
  --ink:#222;
  --muted:#8a8a8a;
  --rule:#cfcfcf;
  --blue:#1a8fd0;
  --teal:#2bb89a;
  --orange:#f07a1c;
  --white:#fff;
}
*{margin:0;padding:0;box-sizing:border-box}
html,body{width:1200px;height:863px;overflow:hidden;background:var(--white)}
body{position:relative;font-family:"Arimo",Helvetica,Arial,sans-serif;color:var(--ink)}
a{color:inherit;text-decoration:none}

.utility-bar{position:absolute;left:0;top:0;width:1200px;height:29px;background:var(--brown-dark)}
.utility-bar a{position:absolute;top:9px;font-size:11.5px;color:var(--white);white-space:nowrap}
.cart-icon{position:absolute;left:1013px;top:7px}

.site-header{position:absolute;left:0;top:29px;width:1200px;height:71px;background:var(--white);box-shadow:0 2px 3px rgba(0,0,0,.12);z-index:2}
.brand{position:absolute;left:211px;top:24px;display:flex;align-items:center;gap:8px;font-size:15px;font-weight:700;color:var(--brown-dark);white-space:nowrap}
.brand-dot{width:12px;height:12px;border-radius:50%;background:var(--brown-dark)}
.main-nav a{position:absolute;top:46px;font-size:10.7px;color:var(--ink);letter-spacing:-.1px;white-space:nowrap}

.brew-question{position:absolute;left:0;top:142px;width:1176px;text-align:center;font-size:16px;font-weight:400;color:#333}

.method-band{position:absolute;left:0;top:212px;width:1200px;height:177px;background:var(--band)}
.method{position:absolute;top:29px;width:104px;margin-left:-46px;text-align:left}
.method svg{display:block}
.method-label{display:block;margin-top:10px;width:84px;text-align:center;font-size:12px;color:#333;white-space:nowrap}

.product{position:absolute;top:451px;width:200px}
.product-photo{width:200px;height:118px}
.product-meta{display:flex;justify-content:space-between;margin-top:13px;font-size:11.5px}
.product-price{color:#333;padding-right:11px}
.product-desc{margin-top:7px;font-size:10.5px;color:var(--muted)}
.product-rule{margin-top:12px;height:1px;background:var(--rule)}

.site-footer{position:absolute;left:0;top:749px;width:1200px;height:81px;background:var(--amber)}
.footer-nav a{position:absolute;top:20px;font-size:12.5px;color:var(--white);white-space:nowrap}
.social{position:absolute;top:20px;width:18px;height:18px;border-radius:50%;background:var(--amber-shade)}
.legal-bar{position:absolute;left:0;top:830px;width:1200px;height:33px;background:var(--brown-dark)}
.legal{position:absolute;right:168px;top:12px;font-size:9.5px;color:var(--copper);white-space:nowrap}
</style>
</head>
<body>

<div class="utility-bar">
  <a href="#" style="left:721px">Register</a>
  <a href="#" style="left:796px">Login</a>
  <a href="#" style="left:857px">Subscriptions</a>
  <a href="#" style="left:960px">Cart ( 0 )</a>
  <svg class="cart-icon" width="17" height="16" viewBox="0 0 17 16" aria-hidden="true">
    <path d="M0 1h3l2.5 9h9L16.5 3H4.5" fill="none" stroke="#fff" stroke-width="1.8" stroke-linejoin="round"/>
    <path d="M4.2 3h12.3l-2 7h-9z" fill="#fff"/>
    <circle cx="6.5" cy="13.5" r="1.6" fill="#fff"/>
    <circle cx="13" cy="13.5" r="1.6" fill="#fff"/>
  </svg>
</div>

<header class="site-header">
  <a href="#" class="brand"><span class="brand-dot"></span>Coffee Meridian</a>
  <nav class="main-nav">
    <a href="#" style="left:554px">HOME</a>
    <a href="#" style="left:608px">BREWING GUIDES</a>
    <a href="#" style="left:720px">SUBSCRIPTIONS</a>
    <a href="#" style="left:825px">MERCHANDISE</a>
    <a href="#" style="left:921px">BLOG</a>
    <a href="#" style="left:973px">OUR STORY</a>
  </nav>
</header>

<h1 class="brew-question">How do you brew your coffee?</h1>

<section class="method-band">
  <svg width="0" height="0" style="position:absolute" aria-hidden="true">
    <defs>
      <linearGradient id="hex-shade" x1="0" y1="0" x2="1" y2="1">
        <stop offset="0" stop-color="#cfcfcf"/>
        <stop offset="1" stop-color="#e9e9e9"/>
      </linearGradient>
      <radialGradient id="tone-glass" cx=".5" cy=".5" r=".5"><stop offset="0" stop-color="#d8d8d8"/><stop offset="1" stop-color="#fff" stop-opacity="0"/></radialGradient>
      <radialGradient id="tone-dark" cx=".5" cy=".5" r=".5"><stop offset="0" stop-color="#3a2b22"/><stop offset=".55" stop-color="#8a7f78"/><stop offset="1" stop-color="#fff" stop-opacity="0"/></radialGradient>
      <radialGradient id="tone-steel" cx=".5" cy=".5" r=".5"><stop offset="0" stop-color="#6d6a68"/><stop offset=".6" stop-color="#b9b6b3"/><stop offset="1" stop-color="#fff" stop-opacity="0"/></radialGradient>
      <radialGradient id="tone-cold" cx=".5" cy=".5" r=".5"><stop offset="0" stop-color="#a86d3c"/><stop offset=".6" stop-color="#dcc0a2"/><stop offset="1" stop-color="#fff" stop-opacity="0"/></radialGradient>
      <radialGradient id="tone-carafe" cx=".5" cy=".5" r=".5"><stop offset="0" stop-color="#c8921e"/><stop offset=".6" stop-color="#eedcb4"/><stop offset="1" stop-color="#fff" stop-opacity="0"/></radialGradient>
      <radialGradient id="tone-nel" cx=".5" cy=".5" r=".5"><stop offset="0" stop-color="#5a4636"/><stop offset=".6" stop-color="#d8cfc5"/><stop offset="1" stop-color="#fff" stop-opacity="0"/></radialGradient>
    </defs>
  </svg>

  <div class="method" style="left:211px">
    <svg width="104" height="112" viewBox="0 0 104 112" role="img" aria-label="Clear drip brewing cone"><polygon points="42,0 84,24 104,48 104,112 62,112 42,96" fill="url(#hex-shade)"/><polygon points="42,0 84,24 84,72 42,96 0,72 0,24" fill="#fff"/><ellipse cx="42" cy="48" rx="28" ry="32" fill="url(#tone-glass)"/></svg>
    <span class="method-label">Drip</span>
  </div>
  <div class="method" style="left:306px">
    <svg width="104" height="112" viewBox="0 0 104 112" role="img" aria-label="Glass plunger press filled with coffee"><polygon points="42,0 84,24 104,48 104,112 62,112 42,96" fill="url(#hex-shade)"/><polygon points="42,0 84,24 84,72 42,96 0,72 0,24" fill="#fff"/><ellipse cx="42" cy="50" rx="22" ry="36" fill="url(#tone-dark)"/></svg>
    <span class="method-label">French Press</span>
  </div>
  <div class="method" style="left:402px">
    <svg width="104" height="112" viewBox="0 0 104 112" role="img" aria-label="Steel espresso machine"><polygon points="42,0 84,24 104,48 104,112 62,112 42,96" fill="url(#hex-shade)"/><polygon points="42,0 84,24 84,72 42,96 0,72 0,24" fill="#fff"/><ellipse cx="42" cy="48" rx="38" ry="32" fill="url(#tone-dark)"/></svg>
    <span class="method-label">Espresso</span>
  </div>
  <div class="method" style="left:498px">
    <svg width="104" height="112" viewBox="0 0 104 112" role="img" aria-label="Stovetop moka pot"><polygon points="42,0 84,24 104,48 104,112 62,112 42,96" fill="url(#hex-shade)"/><polygon points="42,0 84,24 84,72 42,96 0,72 0,24" fill="#fff"/><ellipse cx="42" cy="48" rx="24" ry="36" fill="url(#tone-steel)"/></svg>
    <span class="method-label">Moka Pot</span>
  </div>
  <div class="method" style="left:594px">
    <svg width="104" height="112" viewBox="0 0 104 112" role="img" aria-label="Tall glass of iced coffee"><polygon points="42,0 84,24 104,48 104,112 62,112 42,96" fill="url(#hex-shade)"/><polygon points="42,0 84,24 84,72 42,96 0,72 0,24" fill="#fff"/><ellipse cx="42" cy="48" rx="20" ry="36" fill="url(#tone-cold)"/></svg>
    <span class="method-label">Cold Brew</span>
  </div>
  <div class="method" style="left:690px">
    <svg width="104" height="112" viewBox="0 0 104 112" role="img" aria-label="Glass hourglass carafe with wooden collar"><polygon points="42,0 84,24 104,48 104,112 62,112 42,96" fill="url(#hex-shade)"/><polygon points="42,0 84,24 84,72 42,96 0,72 0,24" fill="#fff"/><ellipse cx="42" cy="48" rx="22" ry="36" fill="url(#tone-carafe)"/></svg>
    <span class="method-label">Carafe Pour</span>
  </div>
  <div class="method" style="left:786px">
    <svg width="104" height="112" viewBox="0 0 104 112" role="img" aria-label="Cloth filter over a glass server"><polygon points="42,0 84,24 104,48 104,112 62,112 42,96" fill="url(#hex-shade)"/><polygon points="42,0 84,24 84,72 42,96 0,72 0,24" fill="#fff"/><ellipse cx="42" cy="48" rx="32" ry="34" fill="url(#tone-nel)"/></svg>
    <span class="method-label">Nel Drip</span>
  </div>
  <div class="method" style="left:882px">
    <svg width="104" height="112" viewBox="0 0 104 112" role="img" aria-label="Glass siphon brewer on a stand"><polygon points="42,0 84,24 104,48 104,112 62,112 42,96" fill="url(#hex-shade)"/><polygon points="42,0 84,24 84,72 42,96 0,72 0,24" fill="#fff"/><ellipse cx="42" cy="48" rx="20" ry="40" fill="url(#tone-steel)"/></svg>
    <span class="method-label">Siphoh</span>
  </div>
  <div class="method" style="left:978px">
    <svg width="104" height="112" viewBox="0 0 104 112" role="img" aria-label="Plunger tube brewer over a mug"><polygon points="42,0 84,24 104,48 104,112 62,112 42,96" fill="url(#hex-shade)"/><polygon points="42,0 84,24 84,72 42,96 0,72 0,24" fill="#fff"/><ellipse cx="42" cy="48" rx="20" ry="40" fill="url(#tone-dark)"/></svg>
    <span class="method-label">Press Tube</span>
  </div>
</section>

<article class="product" style="left:170px">
  <div class="product-photo" role="img" aria-label="French press beside a sack of roasted beans" style="background:radial-gradient(ellipse 40% 55% at 28% 55%,rgba(20,10,4,.75),transparent 70%),radial-gradient(ellipse 45% 50% at 80% 60%,#a8683a,transparent 75%),linear-gradient(180deg,#4a2412 0%,#6e3a1c 55%,#8a4c26 80%,#5a2c14 100%)"></div>
  <div class="product-meta"><span style="color:var(--blue)">Alta Serena</span><span class="product-price">$19.00 / 1 lb</span></div>
  <p class="product-desc">Heavy, comforting, deeply fruited</p>
  <div class="product-rule"></div>
</article>
<article class="product" style="left:388px">
  <div class="product-photo" role="img" aria-label="Close-up of kraft coffee bags" style="background:radial-gradient(ellipse 35% 45% at 62% 55%,#c7a676,transparent 75%),linear-gradient(90deg,#3e3220 0%,#6a5636 18%,#7a6440 30%,#a88a5c 42%,#b8996a 70%,#a48658 100%)"></div>
  <div class="product-meta"><span style="color:var(--teal)">Alta Serena</span><span class="product-price">$19.00 / 1 lb</span></div>
  <p class="product-desc">Heavy, comforting, deeply fruited</p>
  <div class="product-rule"></div>
</article>
<article class="product" style="left:606px">
  <div class="product-photo" role="img" aria-label="Burlap sacks spilling coffee beans on wood" style="background:radial-gradient(ellipse 30% 35% at 28% 55%,#d9cbb4,transparent 75%),radial-gradient(ellipse 30% 35% at 62% 52%,#d2c2a8,transparent 75%),radial-gradient(ellipse 50% 20% at 55% 88%,#3a2012,transparent 80%),linear-gradient(180deg,#b07440 0%,#c79868 45%,#b89070 70%,#8a6446 100%)"></div>
  <div class="product-meta"><span style="color:var(--brown-deep)">Alta Serena</span><span class="product-price">$19.00 / 1 lb</span></div>
  <p class="product-desc">Heavy, comforting, deeply fruited</p>
  <div class="product-rule"></div>
</article>
<article class="product" style="left:822px">
  <div class="product-photo" role="img" aria-label="Three kraft coffee bags on a dark background" style="background:radial-gradient(ellipse 14% 48% at 24% 62%,#c2a274,transparent 90%),radial-gradient(ellipse 16% 52% at 51% 60%,#cdae80,transparent 90%),radial-gradient(ellipse 14% 48% at 78% 62%,#c2a274,transparent 90%),linear-gradient(180deg,#18222c,#202c36)"></div>
  <div class="product-meta"><span style="color:var(--orange);padding-left:2px">Alta Serena</span><span class="product-price">$19.00 / 1 lb</span></div>
  <p class="product-desc" style="padding-left:2px">Heavy, comforting, deeply fruited</p>
  <div class="product-rule" style="margin-left:2px"></div>
</article>

<footer class="site-footer">
  <nav class="footer-nav">
    <a href="#" style="left:192px">Contact</a>
    <a href="#" style="left:271px">Special Orders</a>
    <a href="#" style="left:388px">Wholesale</a>
    <a href="#" style="left:480px">Press</a>
    <a href="#" style="left:545px">FAQ</a>
  </nav>
  <a href="#" class="social" style="left:945px" aria-label="Social profile one"></a>
  <a href="#" class="social" style="left:976px" aria-label="Social profile two"></a>
  <a href="#" class="social" style="left:1005px" aria-label="Social profile three"></a>
</footer>
<div class="legal-bar">
  <p class="legal">COPY RIGHTS 2014, ALL RIGHTS RESERVED BY COFFEE MERIDIAN</p>
</div>

</body>
</html>
```